Update New Business Card - For Start Up

I need to update my business card, I have our old version for example. I would like to keep to the same colors and theme. We are a threat reporting and case management tool for corporations and educational institutions.

Target Market(s)

Corporate Security and Human Resources, School Administrators and Superintendents.

Industry/Entity Type

Physical Security and Technology.

Contact Information for Business Card

My Name, Founder/CEO, phone number 555-214-6082, Logo, Web...

Colors
0054AA
0677BA
7BADD7
CADEEF
E8F1F8

Requirements
Must have
• Something new and trendy.

```html
<!DOCTYPE html>
<html lang="en">
<head>
<meta charset="utf-8">
<title>Vantorel Business Card</title>
<link href="https://fonts.googleapis.com/css2?family=Montserrat:wght@700&family=Mulish:wght@400;500&display=swap" rel="stylesheet">
<style>
  :root {
    --stage: #3b3b3b;
    --navy: #29388f;
    --brand-deep: #0054aa;
    --brand-mid: #0677ba;
    --sky: #7badd7;
    --mist: #cadeef;
    --frost: #e8f1f8;
    --ink: #111111;
    --title-blue: #2a3b9a;
  }
  * { box-sizing: border-box; margin: 0; padding: 0; }
  html, body { width: 1200px; height: 900px; overflow: hidden; }
  body { background: var(--stage); position: relative; font-family: "Mulish", sans-serif; }

  .card { position: absolute; overflow: hidden; }
  .card--front { left: 271px; top: 47px; width: 673px; height: 385px; }
  .card--back { left: 271px; top: 450px; width: 675px; height: 386px; }

  .card__pattern { position: absolute; inset: 0; }
  .card--front .card__pattern {
    background:
      radial-gradient(ellipse 40% 60% at 50% 25%, rgba(255,255,255,0.85), transparent 70%),
      radial-gradient(ellipse 30% 40% at 50% 90%, rgba(255,255,255,0.8), transparent 70%),
      linear-gradient(100deg, #9cc2f4 0%, var(--mist) 40%, var(--frost) 55%, #b9d5f5 80%, #a7c8f3 100%);
  }
  .card--back .card__pattern {
    background:
      linear-gradient(180deg, #8fb7f3 0%, #a6c8f5 45%, var(--mist) 70%, var(--frost) 100%);
  }

  .brand { position: absolute; display: flex; align-items: center; gap: 16px; }
  .brand__dot {
    width: 80px; height: 80px; border-radius: 50%;
    background: var(--navy);
  }
  .brand__name {
    font-family: "Mulish", sans-serif; font-weight: 400;
    font-size: 40px; letter-spacing: 7px; color: var(--navy);
    text-transform: uppercase;
  }
  .card--front .brand { left: 149px; top: 59px; }
  .card--back .brand { left: 151px; top: 137px; }

  .divider { position: absolute; left: 0; right: 0; top: 172px; height: 7px;
    background: linear-gradient(90deg, var(--navy), var(--brand-mid)); }

  .identity { position: absolute; right: 341px; top: 237px; text-align: right; }
  .identity__name { font-family: "Montserrat", sans-serif; font-weight: 700;
    font-size: 33px; color: var(--ink); line-height: 1; letter-spacing: -0.3px; }
  .identity__title { font-size: 15px; color: var(--title-blue); letter-spacing: 0.4px;
    margin-top: 6px; margin-right: 4px; text-transform: uppercase; }

  .rule { position: absolute; left: 358px; top: 236px; width: 2px; height: 77px; background: var(--navy); }

  .contacts { position: absolute; left: 376px; top: 237px; list-style: none; }
  .contacts__item { display: flex; align-items: center; height: 25.5px;
    font-size: 16px; color: var(--ink); letter-spacing: 0.2px; }
  .contacts__icon { width: 14px; height: 14px; margin-right: 13px; fill: var(--navy); flex: none; }

  .base-band { position: absolute; left: 0; right: 0; bottom: 0; height: 27px;
    background: linear-gradient(90deg, var(--navy), var(--brand-mid)); }
</style>
</head>
<body>

<section class="card card--front">
  <div class="card__pattern" role="img" aria-label="Soft blue faceted triangle background pattern"></div>
  <div class="brand">
    <span class="brand__dot"></span>
    <span class="brand__name">Vantorel</span>
  </div>
  <div class="divider"></div>
  <div class="identity">
    <p class="identity__name">Dana Whitfield</p>
    <p class="identity__title">Chief Executive Officer</p>
  </div>
  <div class="rule"></div>
  <ul class="contacts">
    <li class="contacts__item">
      <svg class="contacts__icon" viewBox="0 0 24 24"><path d="M6.6 10.8a15.1 15.1 0 0 0 6.6 6.6l2.2-2.2c.3-.3.7-.4 1-.2 1.1.4 2.3.6 3.6.6.6 0 1 .4 1 1V20c0 .6-.4 1-1 1A17 17 0 0 1 3 4c0-.6.4-1 1-1h3.5c.6 0 1 .4 1 1 0 1.3.2 2.5.6 3.6.1.3 0 .7-.2 1z"/></svg>
      888-899-3799 | 555-214-6082
    </li>
    <li class="contacts__item">
      <svg class="contacts__icon" viewBox="0 0 24 24"><path d="M2 5h20v14H2z M2 5l10 8 10-8" /></svg>
      dana@vantorel.co
    </li>
    <li class="contacts__item">
      <svg class="contacts__icon" viewBox="0 0 24 24"><circle cx="12" cy="12" r="10" fill="none" stroke="var(--navy)" stroke-width="2"/><path d="M2 12h20M12 2c3 3 3 17 0 20M12 2c-3 3-3 17 0 20" fill="none" stroke="var(--navy)" stroke-width="1.6"/></svg>
      www.vantorel.com
    </li>
  </ul>
</section>

<section class="card card--back">
  <div class="card__pattern" role="img" aria-label="Soft blue faceted triangle background pattern"></div>
  <div class="brand">
    <span class="brand__dot"></span>
    <span class="brand__name">Vantorel</span>
  </div>
  <div class="base-band"></div>
</section>

</body>
</html>
```